Egle Marcinkute - Armonici CD

We need a design for the CD cover.  Front and Back.  This is a classical music - soprano + orchestra cd release.  Needs to be a creative/traditional design.  we attach several photos of the artists for you to choose from. please feel free to use any graphics from www.thearmonici-example.org, or www.wbfenwickopera-example.org
Please see the records.thearmonici-example.org for the past submissions/projects.

Target Market(s)
Classical music lovers, mature audiences
Requirements
Must have
- Egle Marcinkute, soprano
Hartwell Armonici Chamber Orchestra
Tomas Brekvold, conductor
Logo of the Opera (FWO) (attached)
Logo of the Orchestra (attached)
Logo of the label (attached)
lists of tracks:
1 Vola, vola mia stella! from I fuochi di Serrano, Callari
2 Lume Serena from Gandolfo, Callari
3 Cantai d'Amore from Lidia, Rambetti
4 Una sera torneremo - Signora Gelsomina, Rambetti
5 Io son chiamata Lulù - La Pèlerine, Rambetti
6 Pura Stella from Tessaria, Tordassi
7 Ortensia's Aria from Rosanne, Lemarc
8 Tendi cuor from Il ritorno di Lisandro, Kreubel
9 Ove fuggono i dolci giorni, The Countess's aria from Il Ritorno di Lisandro - Kreubel
Nice to have
- We want a modern, attractive, perhaps provocative design. Be creative, please feel free to use any graphics from www.thearmonici-example.org, or www.wbfenwickopera-example.org

```html
<!DOCTYPE html>
<html lang="en">
<head>
<meta charset="utf-8">
<title>Armonici CD – back cover track listing</title>
<link href="https://fonts.googleapis.com/css2?family=Cormorant+Garamond:wght@500&family=Pinyon+Script&display=swap" rel="stylesheet">
<style>
  :root {
    --band: #000000;
    --sepia-dark: #3a2a1a;
    --sepia-mid: #6e5236;
    --sepia-light: #a88a62;
    --ink-cream: #efe1c4;
    --shadow: rgba(20, 10, 0, 0.9);
    --credit: #f2eadb;
  }
  * { margin: 0; padding: 0; box-sizing: border-box; }
  html, body { width: 1200px; height: 1200px; overflow: hidden; background: var(--band); }
  .cover {
    position: relative;
    width: 1200px;
    height: 1200px;
    background: var(--band);
    overflow: hidden;
  }
  .artwork {
    position: absolute;
    left: 0; top: 73px;
    width: 1200px; height: 1040px;
    background:
      radial-gradient(ellipse 380px 420px at 900px 420px, rgba(232,220,198,0.55), rgba(232,220,198,0) 70%),
      radial-gradient(ellipse 300px 260px at 1050px 760px, rgba(232,220,198,0.45), rgba(232,220,198,0) 70%),
      radial-gradient(ellipse 700px 600px at 420px 480px, var(--sepia-light), var(--sepia-mid) 60%, var(--sepia-dark) 100%);
  }
  .tracklist {
    position: absolute;
    left: 31px; top: 0;
    list-style: none;
  }
  .track {
    position: absolute;
    left: 0;
    white-space: nowrap;
    font-family: "Cormorant Garamond", serif;
    font-weight: 500;
    font-size: 40px;
    line-height: 1;
    color: var(--ink-cream);
    text-shadow: 2px 2px 3px var(--shadow), 0 0 6px rgba(0,0,0,0.6);
  }
  .composer {
    font-family: "Pinyon Script", cursive;
    font-size: 54px;
    margin-left: 4px;
  }
  .credit {
    position: absolute;
    font-family: "Cormorant Garamond", serif;
    font-weight: 500;
    font-size: 18px;
    line-height: 1;
    color: var(--credit);
    white-space: nowrap;
  }
  .credit-orchestra { left: 745px; top: 1108px; }
  .credit-opera { left: 900px; top: 1108px; }
  .credit-label { left: 1060px; top: 1108px; }
</style>
</head>
<body>
<div class="cover">
  <div class="artwork" role="img" aria-label="Sepia sheet music background with a conductor raising his baton, surrounded by soft bokeh light"></div>

  <ol class="tracklist">
    <li class="track" style="top:230px">1. Vola, vola mia stella! from I fuochi di Serrano, <span class="composer">Callari</span></li>
    <li class="track" style="top:311px">2. Lume Serena from Gandolfo, <span class="composer">Callari</span></li>
    <li class="track" style="top:392px">3. Cantai d'Amore from Lidia, <span class="composer">Rambetti</span></li>
    <li class="track" style="top:472px">4. Una sera torneremo - Signora Gelsomina, <span class="composer">Rambetti</span></li>
    <li class="track" style="top:553px">5. Io son chiamata Lulù - La Pèlerine, <span class="composer">Rambetti</span></li>
    <li class="track" style="top:634px">6. Pura Stella from Tessaria, <span class="composer">Tordassi</span></li>
    <li class="track" style="top:715px">7. Ortensia's Aria from Rosanne, <span class="composer">Lemarc</span></li>
    <li class="track" style="top:795px">8. Tendi cuor from Il ritorno di Lisandro, <span class="composer">Kreubel</span></li>
    <li class="track" style="top:876px">9. Ove fuggono i dolci giorni,<br>The Countess's aria from Il Ritorno di Lisandro - <span class="composer">Kreubel</span></li>
  </ol>

  <div class="credit credit-orchestra">Hartwell Armonici</div>
  <div class="credit credit-opera">Fenwick Lyric Opera</div>
  <div class="credit credit-label">Armonici Records</div>
</div>
</body>
</html>
```